Tulips on Tandems: Ladies Night at a Bike Shop Post Card Promo

Meadowgate Pedal is a well respected bike shop. We need a postcard design to promote a Ladies Night at a local bike shop. It is a evening that helps educate women about cycling and what equipment they need. It is a festive and fun evening with a fashion show! This card will not be mailed so there is no need to include space for address in the back.

Target Market(s)

Women ages 25 and up

Industry/Entity Type

Recreation

Font styles to use
Sans Serif

Requirements
Must have
• Meadowgate Pedals Logo
• Tulips on Tandems Logo
Should not have
• Photos of young girls on it - the audience is older. Also the audience is mixed in terms of athletic ability and size so I don't want imagery that will intimidate folks from attending - thinking that it will be too elite for them. It is for beginners to advanced cyclists!

```html
<!DOCTYPE html>
<html lang="en">
<head>
<meta charset="utf-8">
<title>Tulips on Tandems – Postcard</title>
<link rel="stylesheet" href="https://fonts.googleapis.com/css2?family=Montserrat:wght@600;700&family=Open+Sans:wght@400;600;700&display=swap">
<style>
  :root {
    --page-bg: #1a1a1a;
    --sky-light: #e3e9f0;
    --sky-mid: #c9d4e0;
    --rock: #cbc0ab;
    --sky-faded: #e8ecf1;
    --sky-faded-mid: #dde3ea;
    --rock-faded: #dcd6cb;
    --ink: #2b2b2b;
    --band: rgba(58, 56, 56, 0.92);
    --band-text: #ffffff;
    --band-accent: #d6c9a6;
    --box-bg: #ffffff;
    --logo-grey: #555555;
    --logo-pink: #e0208c;
  }
  * { box-sizing: border-box; margin: 0; padding: 0; }
  html, body { width: 1200px; height: 1024px; overflow: hidden; }
  body {
    background: var(--page-bg);
    font-family: "Open Sans", Arial, sans-serif;
    color: var(--ink);
    position: relative;
  }
  .postcard {
    position: absolute;
    left: 268px;
    width: 664px;
    height: 470px;
    overflow: hidden;
    box-shadow: 0 8px 24px rgba(0,0,0,0.5);
  }
  .postcard--back { top: 26px; }
  .postcard--front { top: 528px; }

  .photo {
    position: absolute;
    inset: 0;
    background: linear-gradient(180deg, var(--sky-light) 0%, var(--sky-mid) 62%, var(--rock) 100%);
  }
  .postcard--back .photo {
    background: linear-gradient(180deg, var(--sky-faded) 0%, var(--sky-faded-mid) 65%, var(--rock-faded) 100%);
  }

  /* back side */
  .event-details {
    position: absolute;
    left: 38px; top: 34px;
    font-weight: 700;
    font-size: 15px;
    line-height: 1.3;
  }
  .highlights {
    position: absolute;
    left: 88px; top: 150px;
    width: 540px;
    background: var(--box-bg);
    border: 1.5px solid var(--ink);
    padding: 12px 18px 14px;
    text-align: center;
    font-size: 14.5px;
    line-height: 1.35;
  }
  .highlights__title { font-weight: 700; font-size: 18px; margin-bottom: 2px; }
  .highlights__cta { font-weight: 700; font-size: 17px; margin-top: 6px; line-height: 1.3; }

  .logo-row {
    position: absolute;
    left: 0; right: 0; bottom: 36px;
    display: flex;
    justify-content: center;
    gap: 34px;
    align-items: center;
  }
  .brand-name {
    display: flex;
    align-items: center;
    gap: 10px;
    font-weight: 700;
    font-size: 20px;
    background: rgba(255,255,255,0.75);
    padding: 12px 18px;
  }
  .brand-name--shop { color: var(--logo-grey); }
  .brand-name--event { color: var(--logo-pink); }

  /* front side */
  .headline {
    position: absolute;
    left: 36px; top: 44px;
    font-family: "Montserrat", Arial, sans-serif;
    font-weight: 600;
    font-size: 31px;
    line-height: 1.25;
    letter-spacing: 1.5px;
    color: var(--ink);
    text-transform: uppercase;
  }
  .info-band {
    position: absolute;
    left: 0; right: 0; bottom: 0;
    height: 124px;
    background: var(--band);
    padding: 20px 12px 0;
    text-align: center;
    color: var(--band-text);
    font-size: 18px;
    line-height: 1.32;
  }
  .info-band__when {
    color: var(--band-accent);
    font-size: 16.5px;
    white-space: nowrap;
    margin-top: 2px;
  }
</style>
</head>
<body>

<section class="postcard postcard--back" aria-label="Postcard back">
  <div class="photo" role="img" aria-label="Faded photo of a woman cheering beside her bicycle on rocks under a pale sky"></div>

  <div class="event-details">
    <p>Thursday, April 21, 2016 &nbsp;6:30pm – 9pm</p>
    <p>Meadowgate Pedals</p>
    <p>418 North Linden Ave, Aldermoor, CO</p>
    <p>555-014-2738 &nbsp;www.meadowgatepedals.com</p>
  </div>

  <div class="highlights">
    <p class="highlights__title">Event highlights:</p>
    <p>Brightrita Bar hosted by Brightwater Labs; Chocolate Fountain; Chair Massages; Cycling jewelry; and Shopping! Plus Kestrel Sports &amp; Bike Aldermoor will be onsite to provide a special challenge!</p>
    <p class="highlights__cta">Register online &amp; receive a goody bag:<br>https://tulipsontandemsmp.ticketwell.com</p>
  </div>

  <div class="logo-row">
    <div class="brand-name brand-name--shop">
      <svg width="14" height="14" aria-hidden="true"><circle cx="7" cy="7" r="7" fill="#555555"/></svg>
      Meadowgate Pedals
    </div>
    <div class="brand-name brand-name--event">
      <svg width="14" height="14" aria-hidden="true"><rect width="14" height="14" fill="#e0208c"/></svg>
      Tulips on Tandems
    </div>
  </div>
</section>

<section class="postcard postcard--front" aria-label="Postcard front">
  <div class="photo" role="img" aria-label="Photo of a woman in a helmet cheering with arms raised beside her mountain bike on rocky ground"></div>

  <h1 class="headline">Let’s get<br>this cycling<br>season started<br>the right way!</h1>

  <div class="info-band">
    <p>Learn about the latest trends in cycling apparel, bicycles, nutrition,<br>hydration and what you need to feel confident on the bicycle.</p>
    <p class="info-band__when">Thursday, April 21, 2016 - 6:30pm – 9pm - Meadowgate Pedals - Aldermoor</p>
  </div>
</section>

</body>
</html>
```